Webdesign für eine Metallfirma
Zielgruppe
Der Auftraggegeber ist eine Metallfirma, welche sich mit Metallbau, Parktechnik,Preßwerkzeugen,Stadtmöblierung
und neu mit Erneuerbaren Energien beschäftigt.
Zielgruppe sind sowohl private als auch geschäftliche Partner, aber auch Städte und Gemeinden.
Aufgabenstellung
- das Layout benötigen wir als PSD
- nur die Startseite soll gelayoutet werden
- die vorherrschende Farbe orientiert sich am Logo, gewünscht ist eine weitere Farbe, da verlassen wir uns auf Ihren Geschmack (siehe anbei)
- die Inhalte der beiden angegebenen Webseiten sollen zusammengeführt werden (siehe unten)
- bitte lassen Sie die Navigationspunkte in allen Ebenen aufklappen

```html
<!DOCTYPE html>
<html lang="de">
<head>
<meta charset="utf-8">
<title>Stelvar Metall- und Anlagenbau – Startseite</title>
<link rel="stylesheet" href="https://fonts.googleapis.com/css2?family=PT+Sans:wght@400;700&family=Poppins:wght@300;400&display=swap">
<style>
:root{
  --blue:#3a88d4;
  --ink:#444;
  --line:#e8eef5;
  --bg:#ffffff;
  --stage:#ffffff;
}
*{margin:0;padding:0;box-sizing:border-box}
html,body{width:1200px;height:1200px;overflow:hidden;background:var(--stage)}
.page{position:absolute;left:385px;top:22px;width:378px;height:1161px;background:var(--bg);box-shadow:0 0 6px rgba(0,0,0,.12);font-family:'Poppins',sans-serif;color:var(--ink)}
.page *{position:absolute}
.h{font-family:'PT Sans',sans-serif}
.topbar{right:5px;top:2px;font:italic 4.4px 'PT Sans',sans-serif;color:var(--blue);white-space:nowrap}
.brand{left:10px;top:18px;display:flex;align-items:center;gap:4px}
.brand *{position:static}
.brand-mark{width:12px;height:12px;background:var(--blue)}
.brand-name{font:700 6.6px/1.1 'PT Sans',sans-serif;color:var(--blue)}
.mainnav{top:25px;right:5px;display:flex;gap:8px;font:700 4.2px 'PT Sans',sans-serif;color:#333}
.mainnav span{position:static}
.mainnav .active{color:var(--blue)}
.hero{left:0;top:37px;width:378px;height:157px;background:linear-gradient(100deg,#9b9a8e 0%,#c9b98f 35%,#8d8f93 60%,#b6ad98 100%)}
.catbar{left:0;top:194px;width:378px;height:31px;border-bottom:1.5px solid var(--line)}
.catbar span{top:15px;font:400 6.2px 'PT Sans',sans-serif;color:#555;letter-spacing:.1px;white-space:nowrap}
.center{left:0;width:378px;text-align:center}
.intro-title{top:251px;font-size:8px;color:#555}
.intro-text{top:266px;font:300 6.2px/7.8px 'Poppins',sans-serif;color:#666}
.team{left:11px;top:317px;width:170px;height:122px;background:linear-gradient(180deg,#d9dde0 0%,#6f7377 60%,#3e4650 100%)}
.who-title{left:192px;top:317px;font-size:6.6px;color:#555}
.who-text{left:192px;top:334px;width:165px;font:300 4.1px/6.6px 'Poppins',sans-serif;color:#777}
.btn{left:192px;top:407px;width:72px;height:15.5px;background:var(--blue);color:#fff;font:400 4.1px/15.5px 'Poppins',sans-serif;text-align:center}
.feat{top:466px;width:110px}
.feat svg{left:0;top:6px}
.feat b{left:20px;top:0;font:400 6.6px 'PT Sans',sans-serif;color:#555;white-space:nowrap}
.feat p{left:19px;top:8.5px;width:90px;font:300 4.1px/6.4px 'Poppins',sans-serif;color:#888}
.sec-title{font-size:6.6px;color:#555}
.do-text{top:538px;font:300 4.1px/6.6px 'Poppins',sans-serif;color:#777}
.tile-label{font:700 6.4px 'PT Sans',sans-serif;color:#444}
.tile{width:120px;height:78px}
.news{top:835px;width:95px}
.news b{left:0;top:0;font:400 6.6px 'Poppins',sans-serif;color:#444;white-space:nowrap}
.news p{left:0;top:10px;width:92px;font:300 4.1px/6.6px 'Poppins',sans-serif;color:#888}
.news a{left:0;top:37px;font:300 4.3px 'Poppins',sans-serif;color:var(--blue);text-decoration:none}
.dot{top:898px;width:6.5px;height:6.5px;border-radius:50%;border:.6px solid var(--blue)}
.dot.on{width:7.5px;height:7.5px;top:897.5px;background:var(--blue)}
.band{left:0;top:928px;width:378px;height:62px;background:var(--blue);color:#fff}
.band h2{left:19px;top:18px;font:700 6.6px 'PT Sans',sans-serif;white-space:nowrap}
.band p{left:19px;top:31px;width:240px;font:300 4.1px/5.9px 'Poppins',sans-serif}
.band .mail{left:275px;top:33px;width:88px;height:16px;border:.8px solid #fff;font:700 6.2px/14.5px 'PT Sans',sans-serif;text-align:center}
.contact-title{top:1014px;font:700 6.6px/9px 'PT Sans',sans-serif;color:#555}
.person{top:1056px;font:300 3.6px/6px 'Poppins',sans-serif;color:#666;white-space:nowrap}
.person *{position:static;display:block}
.person .role{color:#888;margin-bottom:6px}
.person .gap{margin-bottom:6px}
.foot-line{left:0;top:1120px;width:378px;height:1px;background:var(--line)}
.foot{top:1132px;font:300 3.4px 'Poppins',sans-serif;color:#777;white-space:nowrap}
.legal{top:1151px;font:300 3.2px 'Poppins',sans-serif;color:#888;white-space:nowrap}
</style>
</head>
<body>
<div class="page">
  <div class="topbar">Tel.: +49 (0) 30 555 480-10 &nbsp; / &nbsp; E-Mail: info@stelvar.example</div>

  <div class="brand"><span class="brand-mark"></span><span class="brand-name">Stelvar Metall- und<br>Anlagenbau GmbH</span></div>

  <nav class="mainnav"><span class="active">HOME</span><span>WER WIR SIND</span><span>PRODUKTE</span><span>KARRIERE</span><span>AKTUELLES</span><span>KONTAKT</span></nav>

  <div class="hero" role="img" aria-label="Foto: zwei lächelnde Mitarbeiter in einer Werkhalle, einer mit gelbem Schutzhelm, einer mit Tablet"></div>

  <div class="catbar">
    <span style="left:6px">METALLBAU</span>
    <span style="left:65px">PARKTECHNIK</span>
    <span style="left:127px">PRESSWERKZEUGE</span>
    <span style="left:206px">STADTMÖBLIERUNG</span>
    <span style="left:285px">ERNEUERBARE ENERGIEN</span>
  </div>

  <div class="center h intro-title">Stelvar - Ihr verlässlicher Partner</div>
  <div class="center intro-text">Wir sind im Metallbau,&nbsp; Parktechnik, Presswerkzeuge,<br>Stadtmöblierung und erneuerbare Energien tätig.<br>Lorem ipsum dolor sit amet, consectetuer adipising elit.</div>

  <div class="team" role="img" aria-label="Foto: Team aus fünf Mitarbeitenden in einem hellen Büro"></div>
  <div class="h who-title">WER WIR SIND</div>
  <p class="who-text">Lorem ipsum dolor sit amet, consectetuer adipiscing elit. Aenean commodo ligula eget dolor. Aenean massa. Cum sociis natoque penatibus et magnis dis parturient montes, nascetur ridiculus mus. Donec quam felis, ultricies nec, pellentesque eu, pretium quis, sem. Nulla consequat massa quis enim. Donec pede justo, fringilla vel, aliquet nec, vulputate eget, arcu. In enim justo, rhoncus ut, imperdiet a, venenatis vitae, justo. Nullam dictum felis eu pede mollis pretium. Integer tincidunt. Cras dapibus.</p>
  <div class="btn">Mehr zum Unternehmen</div>

  <div class="feat" style="left:23px"><svg width="16" height="12" viewBox="0 0 16 12"><path d="M1 6.5l4.5 4.5L15 1" fill="none" stroke="#3a88d4" stroke-width="2.2"/></svg><b>Lorem Ipsum dolor</b><p>Donec quam felis, ultricies nec, pellentesque eu, pretium quis,</p></div>
  <div class="feat" style="left:140px"><svg width="16" height="12" viewBox="0 0 16 12"><path d="M1 6.5l4.5 4.5L15 1" fill="none" stroke="#3a88d4" stroke-width="2.2"/></svg><b>Lorem Ipsum dolor</b><p>Donec quam felis, ultricies nec, pellentesque eu, pretium quis,</p></div>
  <div class="feat" style="left:254px"><svg width="16" height="12" viewBox="0 0 16 12"><path d="M1 6.5l4.5 4.5L15 1" fill="none" stroke="#3a88d4" stroke-width="2.2"/></svg><b>Lorem Ipsum dolor</b><p>Donec quam felis, ultricies nec, pellentesque eu, pretium quis,</p></div>

  <div class="center h sec-title" style="top:518px">WAS WIR TUN</div>
  <div class="center do-text">Donec quam felis, ultricies nec, pellentesque eu, pretium quis, sem.<br>Nulla consequat massa quis enim. Donec pede justo, fringilla vel,<br>aliquet nec, vulputate eget, arcu.</div>

  <div class="tile-label" style="left:5px;top:575px">Metallbau</div>
  <div class="tile" style="left:5px;top:585px;background:linear-gradient(135deg,#e4e6e8,#8f9397 55%,#2e3236)" role="img" aria-label="Foto: gestapelte Aluminiumprofile und Rohre"></div>
  <div class="tile-label" style="left:129px;top:575px">Parktechnik</div>
  <div class="tile" style="left:129px;top:585px;background:linear-gradient(120deg,#1f5fae,#3b7fcf 55%,#d9c3ad)" role="img" aria-label="Foto: Hand steckt Parkticket in einen blauen Parkautomaten"></div>
  <div class="tile-label" style="left:253px;top:575px">Presswerkzeuge</div>
  <div class="tile" style="left:253px;top:585px;background:linear-gradient(110deg,#6e6b66,#c7c1b8 45%,#eeeae5)" role="img" aria-label="Foto: Handwerker verpresst Rohrleitungen an einer Wand"></div>

  <div class="tile-label" style="left:66px;top:674px">Stadtmöblierung</div>
  <div class="tile" style="left:66px;top:684px;background:linear-gradient(180deg,#5a9ad8,#b9d6ef 40%,#3c5d9a 62%,#6f8f4a)" role="img" aria-label="Foto: Solarpark mit Windrädern unter blauem Himmel"></div>
  <div class="tile-label" style="left:191px;top:674px">Erneuerbare Energien</div>
  <div class="tile" style="left:191px;top:684px;background:linear-gradient(180deg,#4d7a3a,#8dbb5e 55%,#a9cf6a)" role="img" aria-label="Foto: weiße Parkbank auf einer grünen Wiese"></div>

  <div class="center h sec-title" style="top:806px">UNSERE NEUIGKEITEN</div>

  <div class="news" style="left:27px;top:836px"><b>LOREM IPSUM DOLOR</b><p>In enim justo, rhoncus ut, imperdiet a, venenatis vitae, justo. Nullam dictum felis eu pede mollis pretium. Integer tincidunt. Cras dapibus</p><a>mehr erfahren</a></div>
  <div class="news" style="left:148px"><b>LOREM IPSUM DOLOR</b><p>In enim justo, rhoncus ut, imperdiet a, venenatis vitae, justo. Nullam dictum felis eu pede mollis pretium. Integer tincidunt. Cras dapibus</p><a>mehr erfahren</a></div>
  <div class="news" style="left:261px;top:836px"><b>LOREM IPSUM DOLOR</b><p>In enim justo, rhoncus ut, imperdiet a, venenatis vitae, justo. Nullam dictum felis eu pede mollis pretium. Integer tincidunt. Cras dapibus</p><a>mehr erfahren</a></div>

  <div class="dot" style="left:175px"></div>
  <div class="dot on" style="left:185px"></div>
  <div class="dot" style="left:196px"></div>

  <section class="band">
    <h2>Sie haben Fragen? Wir beraten Sie gerne. Nehmen Sie Kontakt mit uns auf.</h2>
    <p>Lorem ipsum dolor sit amet, consectetuer adipiscing elit. Aenean commodo ligula eget dolor. Aenean massa. Cum sociis natoque penatibus et magnis dis parturient montes, nascetur ridiculus mus. Donec quam felis,</p>
    <div class="mail">E-Mail schreiben</div>
  </section>

  <div class="center contact-title">Unsere Ansprechpartner in den Fachbereichen stehen Ihnen gerne telefonisch<br>oder per E-Mail zur Verfügung</div>

  <div class="person" style="left:32px"><span class="role">PARKTECHNIK</span><span class="gap">Herr Berger</span><span>Telefon: +49 (0) 30 555 480-21</span><span>E-Mail: t.berger@stelvar.example</span></div>
  <div class="person" style="left:107px"><span class="role">METALLBAU</span><span class="gap">Herr Lange</span><span>Telefon: +49 (0) 30 555 480-22</span><span>E-Mail: m.lange@stelvar.example</span></div>
  <div class="person" style="left:184px"><span class="role">SANITÄRTECHNIK &amp; ERNEUERBARE ENERGIEN</span><span class="gap">Herr Vogt</span><span>Telefon: +49 (0) 30 555 480-23</span><span>E-Mail: a.vogt@stelvar.example</span></div>
  <div class="person" style="left:282px"><span class="role">GESCHÄFTSLEITUNG</span><span>Telefon: +49 (0) 30 555 480-10</span><span>Telefax: +49 (0) 30 555 480-90</span><span>E-Mail: &nbsp;info@stelvar.example</span></div>

  <div class="foot-line"></div>
  <div class="foot" style="left:8px">Stelvar Metall- und Anlagenbau GmbH</div>
  <div class="foot" style="left:110px">Werkstraße 12 | 01234 Musterstadt</div>
  <div class="foot" style="left:196px">Tel.: +49 (0) 30 555 480-10 | Fax: +49 (0) 30 555 480-90</div>
  <div class="foot" style="left:306px">E-Mail: info@stelvar.example</div>
  <div class="legal" style="left:9px">Datenschutz</div>
  <div class="legal" style="left:39px">Impressum</div>
  <div class="legal" style="left:76px">Copyright Stelvar 2022</div>
</div>
</body>
</html>
```